Accounting firm needs a postcard design

We need a postcard design for our accounting office for a advertising campaign mailing we do yearly from a mail list we create. We are a full-service accounting office that has been in business for 35 years. I have attached our logo in different formats along with a document with a description of the services we provide. I have also attached my business card and the business card of our CPA. The business cards will have contact information for the postcard design. The contact email that will need to be on the postcard is contact@harrowledgerworks.com.

```html
<!DOCTYPE html>
<html lang="en">
<head>
<meta charset="utf-8">
<title>Harrow Ledger Works – Postcard</title>
<link rel="stylesheet" href="https://fonts.googleapis.com/css2?family=Poppins:wght@400;500;600;700;800&family=Oswald:wght@500&display=swap">
<style>
  :root {
    --navy: #1b2f6b;
    --navy-deep: #142457;
    --blue: #1c6fb8;
    --blue-bright: #2f8fe0;
    --green: #3f9a2c;
    --green-dark: #2c7a1f;
    --orange: #f39a2b;
    --white: #ffffff;
    --ink: #1d2440;
    --rule: #c9ccd4;
    --page: #ececec;
    --photo-light: #eef4e6;
    --photo-mid: #c9dfb4;
  }
  * { box-sizing: border-box; margin: 0; padding: 0; }
  html, body { width: 783px; height: 1200px; overflow: hidden; }
  body { background: var(--page); font-family: "Poppins", sans-serif; color: var(--ink); position: relative; }

  .card { position: absolute; left: 31px; width: 720px; height: 480px; background: var(--white); box-shadow: 0 3px 10px rgba(0,0,0,.18); overflow: hidden; }
  .card--front { top: 95px; }
  .card--back { top: 615px; }
  .card-art { position: absolute; inset: 0; }

  /* front */
  .brand { position: absolute; left: 0; width: 375px; top: 34px; text-align: center; }
  .brand-name { display: inline-flex; align-items: center; gap: 7px; font-weight: 600; font-size: 15px; letter-spacing: 1.2px; color: var(--navy); }
  .brand-mark { width: 12px; height: 12px; background: var(--green); }
  .brand-tagline { font-size: 6.5px; color: var(--ink); margin-top: 3px; }

  .headline { position: absolute; left: 30px; top: 108px; width: 320px; font-weight: 800; line-height: 1.02; text-transform: uppercase; }
  .headline span { display: block; }
  .headline .h-big { font-size: 38px; color: var(--navy); letter-spacing: .2px; }
  .headline .h-mid { font-size: 23.5px; color: var(--navy); margin-top: 3px; }
  .headline .h-green { font-size: 25px; color: var(--green); margin-top: 3px; }

  .divider { position: absolute; left: 30px; top: 283px; width: 315px; height: 1px; background: var(--rule); }
  .divider::before { content: ""; position: absolute; left: 16px; top: -2px; width: 62px; height: 5px; border-radius: 3px; background: var(--blue); }

  .intro { position: absolute; left: 30px; top: 302px; font-size: 13px; line-height: 1.22; color: var(--ink); }
  .intro b { font-weight: 700; }

  .years-badge { position: absolute; left: 212px; top: 300px; width: 135px; height: 48px; background: var(--navy); border-radius: 8px 0 0 8px; display: flex; align-items: center; padding-left: 10px; gap: 6px; }
  .years-num { font-family: "Oswald", sans-serif; font-weight: 500; font-size: 40px; color: var(--orange); line-height: 1; }
  .years-side { display: flex; flex-direction: column; gap: 3px; }
  .years-lines { height: 8px; border-top: 1px solid var(--white); border-bottom: 1px solid var(--white); width: 56px; }
  .years-word { color: var(--white); font-size: 17px; line-height: 1; }

  .contact { position: absolute; list-style: none; color: var(--white); }
  .contact li { display: flex; align-items: center; gap: 7px; }
  .contact svg { width: 12px; height: 12px; flex: none; }
  .contact--front { left: 30px; top: 383px; font-size: 12.5px; line-height: 1; }
  .contact--front li { height: 22px; }
  .contact--front .phone { font-weight: 600; font-size: 14px; }
  .web-front { position: absolute; left: 500px; top: 436px; color: var(--white); font-size: 11.5px; font-weight: 500; }

  /* back */
  .services { position: absolute; left: 0; top: 0; width: 360px; padding: 20px 20px 0 30px; color: var(--white); }
  .services-title { font-size: 18px; font-weight: 400; margin-bottom: 8px; }
  .services-title b { color: var(--orange); font-weight: 700; }
  .service-list { list-style: none; position: relative; padding-left: 28px; }
  .service-list::before { content: ""; position: absolute; left: 9px; top: 8px; bottom: 40px; width: 1px; background: rgba(255,255,255,.55); }
  .service { position: relative; margin-bottom: 8px; }
  .service-icon { position: absolute; left: -28px; top: -1px; width: 19px; height: 19px; border-radius: 50%; background: var(--white); border: 3px solid var(--green); display: flex; align-items: center; justify-content: center; }
  .service-icon svg { width: 9px; height: 9px; }
  .service h3 { font-size: 11.5px; font-weight: 500; color: var(--blue-bright); line-height: 1.2; margin-bottom: 2px; }
  .service p { font-size: 6.3px; line-height: 1.3; color: var(--white); width: 260px; }

  .contact--back { left: 30px; top: 388px; font-size: 9.5px; }
  .contact--back li { height: 17px; }
  .contact--back svg { width: 10px; height: 10px; }
  .contact--back .phone { font-weight: 600; font-size: 11px; }

  .mail-side .brand-name { font-size: 8.5px; letter-spacing: .6px; gap: 4px; }
  .mail-side .brand-mark { width: 8px; height: 8px; }
  .mail-side .brand-tagline { font-size: 4px; }
  .mail-side { position: absolute; left: 395px; top: 56px; }
  .stamp-box { position: absolute; left: 630px; top: 30px; width: 62px; height: 58px; background: #e4e4e4; }
  .address-lines { position: absolute; left: 397px; top: 202px; width: 300px; }
  .address-lines span { display: block; height: 1px; background: #9da3ad; margin-bottom: 31px; }
</style>
</head>
<body>

<svg width="0" height="0" style="position:absolute" aria-hidden="true">
  <defs>
    <symbol id="icon-phone" viewBox="0 0 24 24"><path fill="#f39a2b" d="M6.6 10.8a15.1 15.1 0 0 0 6.6 6.6l2.2-2.2a1 1 0 0 1 1-.25 11.4 11.4 0 0 0 3.6.57 1 1 0 0 1 1 1V20a1 1 0 0 1-1 1A17 17 0 0 1 3 4a1 1 0 0 1 1-1h3.5a1 1 0 0 1 1 1c0 1.25.2 2.45.57 3.6a1 1 0 0 1-.25 1z"/></symbol>
    <symbol id="icon-mail" viewBox="0 0 24 24"><path fill="#f39a2b" d="M2 5h20v14H2z"/><path fill="none" stroke="#1c4f9a" stroke-width="1.6" d="M2 5l10 8 10-8M2 19l7-7M22 19l-7-7"/></symbol>
    <symbol id="icon-pin" viewBox="0 0 24 24"><path fill="#f39a2b" d="M12 2a7 7 0 0 0-7 7c0 5.2 7 13 7 13s7-7.8 7-13a7 7 0 0 0-7-7zm0 9.5A2.5 2.5 0 1 1 12 6.5a2.5 2.5 0 0 1 0 5z"/></symbol>
    <symbol id="icon-globe" viewBox="0 0 24 24"><g fill="none" stroke="#f39a2b" stroke-width="2"><circle cx="12" cy="12" r="9"/><path d="M3 12h18M12 3c3 3.5 3 14.5 0 18M12 3c-3 3.5-3 14.5 0 18"/></g></symbol>
    <symbol id="icon-tick" viewBox="0 0 24 24"><path fill="none" stroke="#3f9a2c" stroke-width="4" d="M4 12l5 5 11-11"/></symbol>
    <linearGradient id="band-blue" x1="0" y1="0" x2="1" y2="1"><stop offset="0" stop-color="#1c6fb8"/><stop offset="1" stop-color="#1b3a82"/></linearGradient>
    <linearGradient id="swoosh-green" x1="0" y1="1" x2="1" y2="0"><stop offset="0" stop-color="#2c7a1f"/><stop offset=".5" stop-color="#3f9a2c"/><stop offset="1" stop-color="#6cc04a"/></linearGradient>
    <linearGradient id="photo-tone" x1="0" y1="0" x2="0" y2="1"><stop offset="0" stop-color="#c9dfb4"/><stop offset=".55" stop-color="#eef4e6"/><stop offset="1" stop-color="#d9c3a6"/></linearGradient>
    <linearGradient id="panel-navy" x1="0" y1="0" x2="0" y2="1"><stop offset="0" stop-color="#1b3a82"/><stop offset="1" stop-color="#142457"/></linearGradient>
  </defs>
</svg>

<!-- FRONT -->
<section class="card card--front" aria-label="Postcard front">
  <svg class="card-art" viewBox="0 0 720 480" aria-hidden="false">
    <rect x="375" y="250" width="345" height="230" fill="#1b2f6b"/>
    <rect x="375" y="0" width="345" height="270" fill="url(#photo-tone)" role="img" aria-label="Photo: cupped hands sheltering a young seedling growing from a pile of coins"/>
    <path d="M430 480 C395 395 455 300 720 150 L720 178 C500 310 450 400 470 480 Z" fill="#ffffff"/>
    <path d="M378 425 C378 340 470 305 560 292 C650 280 700 240 720 178 L720 220 C695 285 610 312 545 322 C470 335 428 395 446 478 C420 470 390 450 378 425 Z" fill="url(#swoosh-green)"/>
    <path d="M0 366 L330 366 C372 366 392 395 425 480 L0 480 Z" fill="url(#band-blue)"/>
  </svg>

  <div class="brand">
    <div class="brand-name"><span class="brand-mark"></span>HARROW LEDGER WORKS</div>
    <div class="brand-tagline">Tax Preparation &nbsp;|&nbsp; Bookkeeping &nbsp;|&nbsp; Payroll &nbsp;|&nbsp; Entity Formation</div>
  </div>

  <h1 class="headline">
    <span class="h-big">Individualized</span>
    <span class="h-mid">Business and Personal</span>
    <span class="h-green">Accounting Services</span>
    <span class="h-green">You Can Trust.</span>
  </h1>

  <div class="divider"></div>

  <p class="intro"><b>We are a full-service<br>accounting office</b> that<br>has been in business for</p>
  <div class="years-badge">
    <span class="years-num">35</span>
    <span class="years-side"><span class="years-lines"></span><span class="years-word">YEARS</span></span>
  </div>

  <ul class="contact contact--front">
    <li class="phone"><svg><use href="#icon-phone"/></svg>(555) 201-4478</li>
    <li><svg><use href="#icon-mail"/></svg>contact@harrowledgerworks.com</li>
    <li><svg><use href="#icon-pin"/></svg>48 Millbrook Ave, Suite 110 Fairview, TX 75000</li>
  </ul>
  <div class="web-front">www.harrowledgerworks.com</div>
</section>

<!-- BACK -->
<section class="card card--back" aria-label="Postcard back">
  <svg class="card-art" viewBox="0 0 720 480">
    <rect x="0" y="0" width="360" height="480" fill="url(#panel-navy)"/>
    <path d="M0 368 L275 368 C310 368 330 380 345 395 L360 380 L360 480 L0 480 Z" fill="url(#band-blue)"/>
    <path d="M290 390 C265 350 300 320 360 300 L360 312 C310 330 292 360 310 392 Z" fill="#ffffff"/>
    <path d="M268 355 C265 325 300 312 330 305 C345 301 355 292 360 282 L360 300 C345 318 312 325 300 338 C290 350 290 368 300 385 C285 378 270 368 268 355 Z" fill="url(#swoosh-green)"/>
  </svg>

  <div class="services">
    <h2 class="services-title">OUR <b>SERVICES</b></h2>
    <ul class="service-list">
      <li class="service">
        <span class="service-icon"><svg><use href="#icon-tick"/></svg></span>
        <h3>TAX PREPARATION</h3>
        <p>With over 35 years of experience filing tax returns, we are experts in tax preparation. Including Personal Returns, Corporations, LLC's, Partnerships and State Franchise Tax Returns.</p>
      </li>
      <li class="service">
        <span class="service-icon"><svg><use href="#icon-tick"/></svg></span>
        <h3>BOOKKEEPING</h3>
        <p>Let us take over the day-to-day bookkeeping so you can get back to running your business. We offer assistance with LedgerPro setup and provide ongoing bookkeeping services. Including frequent journal entries, accounts payables &amp; receivables, sales tax reporting &amp; payments, account reconciliation, and more.</p>
      </li>
      <li class="service">
        <span class="service-icon"><svg><use href="#icon-tick"/></svg></span>
        <h3>FINANCIAL REPORTING</h3>
        <p>We'll provide easy to understand financial reports that allow you and your team to manage cash flow, create budgets and make forecasting decisions. Depending on your needs, we can provide monthly, quarterly or yearly financial statements.</p>
      </li>
      <li class="service">
        <span class="service-icon"><svg><use href="#icon-tick"/></svg></span>
        <h3>PAYROLL PROCESSING</h3>
        <p>Whether you have 5 employees or 100+, payroll can be an overwhelming and time consuming task. We offer full-service payroll processing. Including employee onboarding, printed or direct deposit checks, quarterly payroll report filing, yearly W-2/W-3 and 1099 printing and filing, and more.</p>
      </li>
    </ul>
  </div>

  <ul class="contact contact--back">
    <li class="phone"><svg><use href="#icon-phone"/></svg>(555) 201-4478</li>
    <li><svg><use href="#icon-mail"/></svg>contact@harrowledgerworks.com</li>
    <li><svg><use href="#icon-pin"/></svg>48 Millbrook Ave, Suite 110 Fairview, TX 75000</li>
    <li><svg><use href="#icon-globe"/></svg>www.harrowledgerworks.com</li>
  </ul>

  <div class="mail-side">
    <div class="brand-name"><span class="brand-mark"></span>HARROW LEDGER WORKS</div>
    <div class="brand-tagline">Tax Preparation | Bookkeeping | Payroll | Entity Formation</div>
  </div>
  <div class="stamp-box"></div>
  <div class="address-lines"><span></span><span></span><span></span><span></span></div>
</section>

</body>
</html>
```